Marrowgate Auctions Business Cards Design Needed

I need a business card design that is modern looking - double sided (maybe just my logo on the back, but open to suggestions) - the overall design is up to you. I want it to be easy to read - not over the top flashy. I already have a company logo which I uploaded so that needs to be used. The colors of my logo are the colors I want on the card... so blue and gray (do need to match the logo colors).

Requirements
Must have
• Would like the card to be sleek, modern and easy to ready

```html
<!DOCTYPE html>
<html lang="en">
<head>
<meta charset="utf-8">
<title>Marrowgate Auctions – Business Cards</title>
<link href="https://fonts.googleapis.com/css2?family=Open+Sans:wght@400;700;800&family=Oswald:wght@400;600&display=swap" rel="stylesheet">
<style>
  :root {
    --brand-blue: #2a76b8;
    --brand-gray: #4a4a4c;
    --card-white: #ffffff;
    --page-bg: #ecebe8;
    --text-white: #ffffff;
  }
  html, body {
    margin: 0;
    padding: 0;
    width: 1200px;
    height: 1200px;
    overflow: hidden;
    background: var(--page-bg);
  }
  .sheet {
    position: relative;
    width: 1200px;
    height: 1200px;
  }
  .card {
    position: absolute;
    left: 150px;
    width: 900px;
    height: 514px;
    box-shadow: 0 6px 18px rgba(0,0,0,0.18);
    overflow: hidden;
  }
  .card--front {
    top: 60px;
    background: var(--brand-blue);
  }
  .card--back {
    top: 626px;
    background: var(--card-white);
  }

  /* Front */
  .front-wordmark {
    position: absolute;
    left: 0;
    right: 0;
    top: 200px;
    display: flex;
    justify-content: center;
    align-items: center;
    gap: 18px;
  }
  .front-wordmark__mark {
    width: 34px;
    height: 34px;
    background: var(--text-white);
  }
  .front-wordmark__name {
    font-family: "Open Sans", sans-serif;
    font-weight: 800;
    font-size: 52px;
    letter-spacing: 2px;
    color: var(--text-white);
    text-transform: uppercase;
  }
  .front-tagline {
    position: absolute;
    left: 0;
    right: 0;
    bottom: 64px;
    text-align: center;
    font-family: "Open Sans", sans-serif;
    font-size: 22px;
    letter-spacing: 1px;
    color: var(--text-white);
  }

  /* Back */
  .back-wordmark {
    position: absolute;
    left: 180px;
    top: 150px;
    display: flex;
    align-items: center;
    gap: 16px;
  }
  .back-wordmark__mark {
    width: 30px;
    height: 30px;
    background: var(--brand-blue);
  }
  .back-wordmark__name {
    font-family: "Open Sans", sans-serif;
    font-weight: 800;
    font-size: 46px;
    letter-spacing: 2px;
    color: var(--brand-blue);
    text-transform: uppercase;
  }
  .accent-bar {
    position: absolute;
    right: 0;
    top: 0;
    width: 26px;
    height: 110px;
    background: var(--brand-blue);
  }
  .person {
    position: absolute;
    right: 56px;
    top: 26px;
    text-align: right;
  }
  .person__name {
    font-family: "Oswald", sans-serif;
    font-weight: 600;
    font-size: 40px;
    line-height: 1;
    color: var(--brand-gray);
    text-transform: uppercase;
  }
  .person__title {
    margin-top: 6px;
    font-family: "Oswald", sans-serif;
    font-weight: 400;
    font-size: 20px;
    color: var(--brand-blue);
    text-transform: uppercase;
  }
  .contact {
    position: absolute;
    left: 60px;
    bottom: 48px;
    margin: 0;
    padding: 0;
    list-style: none;
    font-family: "Open Sans", sans-serif;
    font-size: 24px;
    color: var(--brand-gray);
  }
  .contact__item {
    display: flex;
    align-items: center;
    gap: 14px;
    line-height: 38px;
  }
  .contact__icon {
    width: 20px;
    height: 20px;
    flex: none;
  }
</style>
</head>
<body>
<main class="sheet">

  <section class="card card--front" aria-label="Card front">
    <div class="front-wordmark">
      <span class="front-wordmark__mark"></span>
      <span class="front-wordmark__name">Marrowgate Auctions</span>
    </div>
    <p class="front-tagline">Improving Charity Auctions Nationwide.</p>
  </section>

  <section class="card card--back" aria-label="Card back">
    <div class="accent-bar"></div>
    <div class="person">
      <div class="person__name">Corin Wexley</div>
      <div class="person__title">Owner / President</div>
    </div>

    <div class="back-wordmark">
      <span class="back-wordmark__mark"></span>
      <span class="back-wordmark__name">Marrowgate Auctions</span>
    </div>

    <ul class="contact">
      <li class="contact__item">
        <svg class="contact__icon" viewBox="0 0 24 24" aria-hidden="true">
          <path fill="#2a76b8" d="M6.6 10.8a15.1 15.1 0 0 0 6.6 6.6l2.2-2.2a1 1 0 0 1 1-.25 11.4 11.4 0 0 0 3.6.57 1 1 0 0 1 1 1V20a1 1 0 0 1-1 1A17 17 0 0 1 3 4a1 1 0 0 1 1-1h3.5a1 1 0 0 1 1 1c0 1.25.2 2.45.57 3.57a1 1 0 0 1-.25 1z"/>
        </svg>
        <span>+702-555-0148</span>
      </li>
      <li class="contact__item">
        <svg class="contact__icon" viewBox="0 0 24 24" aria-hidden="true">
          <rect x="2" y="5" width="20" height="14" rx="1.5" fill="#2a76b8"/>
          <path d="M3 6.5l9 6.5 9-6.5" fill="none" stroke="#ffffff" stroke-width="1.6"/>
        </svg>
        <span>marrowgateauctions@mail.com</span>
      </li>
      <li class="contact__item">
        <svg class="contact__icon" viewBox="0 0 24 24" aria-hidden="true">
          <circle cx="12" cy="12" r="9.5" fill="none" stroke="#2a76b8" stroke-width="2"/>
          <path d="M2.5 12h19M12 2.5c3 3 3 16 0 19M12 2.5c-3 3-3 16 0 19" fill="none" stroke="#2a76b8" stroke-width="1.5"/>
        </svg>
        <span>www.bidharbor.com</span>
      </li>
    </ul>
  </section>

</main>
</body>
</html>
```